Real Estate Seller Financing Postcard

I need a postcard that lays out these options contained in the notes that grabs attention, explains the two options easily and is eye-catching. The front needs to have the percentages on it and information about it and on the other side One side exact Text is:
"Monthly income without tenant headaches" in big letters. Also on front "Get
110%
add an "or"
160% of market value for your property. ". The percentages should be displayed and that is not to be a sentence of text. Other side text: I need bullets points for these "Formal protection as a lien holder against home
No commission or closing cost
Fast closings possible
Property taken as is so no repairs.

Add to the top of the back in "It’s simple. I am a new investor without down payment capital who still want to double our portfolio this year to grow our portfolio."
Here are the two options that are to be the largest part of the back
Option 1, you can receive 80% now cash and 30% over a short period of time including interest.

Option 2, where act like a bank allowing you to make 150% if you finance the whole property(ies). No gimmicks and surprises, just simple unconventional financing.

Include Logo Somewhere

Target Market(s)

Property Owners Wanting to Sell Their Property

Industry/Entity Type

Real Estate Investing

Requirements
Must have
• The options promiment and each side with its respective information. Must have logo somewhere
Nice to have
• The options in color other than black.
Should not have
• A picture of money on the front. Any other image is okay.

```html
<!DOCTYPE html>
<html lang="en">
<head>
<meta charset="UTF-8">
<title>Seller Financing Postcard</title>
<link href="https://fonts.googleapis.com/css2?family=Montserrat:ital,wght@0,400;0,500;0,600;0,700;1,600&display=swap" rel="stylesheet">
<style>
  :root {
    --stage: #867e7e;
    --cream: #f5ece2;
    --paper: #ffffff;
    --brand-blue: #2673e8;
    --ink: #111111;
    --body-ink: #1c1c1c;
    --accent-orange: #f0a04b;
    --skyline: #fdf2e4;
    --logo-blue: #1c3f8f;
  }
  * { margin: 0; padding: 0; box-sizing: border-box; }
  html, body { width: 1200px; height: 1200px; overflow: hidden; }
  body {
    background: var(--stage);
    font-family: "Montserrat", sans-serif;
    position: relative;
  }
  .card { position: absolute; overflow: hidden; }
  .card--front { left: 281px; top: 94px; width: 657px; height: 500px; background: var(--cream); }
  .card--back { left: 281px; top: 625px; width: 659px; height: 502px; background: var(--paper); }

  .front-band { position: absolute; inset: 0; }
  .headline {
    position: absolute; left: 35px; top: 32px;
    font-size: 41.5px; line-height: 50px; color: var(--ink); font-weight: 500;
  }
  .headline .hl-blue { color: var(--brand-blue); font-weight: 700; }
  .headline strong { font-weight: 700; }
  .benefits {
    position: absolute; left: 36px; top: 209px; width: 250px;
    list-style: none; font-size: 13.2px; line-height: 16px; color: var(--body-ink);
  }
  .benefits li::before { content: "· "; }

  .city-art {
    position: absolute; left: 170px; top: 110px; width: 460px; height: 380px;
    background: radial-gradient(closest-side, rgba(255,255,255,0.75), rgba(236,240,248,0.45) 55%, rgba(255,255,255,0) 100%);
  }

  .pct { position: absolute; color: var(--accent-orange); font-weight: 600; line-height: 1; }
  .pct sup { font-size: 0.55em; vertical-align: top; position: relative; top: 2px; }
  .pct--100 { left: 285px; top: 240px; font-size: 34px; }
  .pct--110 { left: 351px; top: 155px; font-size: 38px; }
  .pct--160 { left: 436px; top: 78px; font-size: 40px; }
  .pct-caption {
    position: absolute; left: 515px; top: 101px;
    color: var(--accent-orange); font-weight: 700; font-size: 16px; line-height: 20px;
  }

  .skyline {
    position: absolute; left: 0; bottom: 0; width: 100%; height: 230px;
    background: linear-gradient(to bottom, rgba(253,242,228,0), var(--skyline) 45%);
  }
  .intro {
    position: absolute; left: 42px; top: 67px; width: 510px;
    color: var(--brand-blue); font-style: italic; font-weight: 600;
    font-size: 19.8px; line-height: 24px;
  }
  .option {
    position: absolute; left: 42px; width: 540px;
    font-size: 16.4px; line-height: 20px; color: var(--body-ink);
  }
  .option--one { top: 170px; }
  .option--two { top: 230px; }

  .brand {
    position: absolute; left: 46px; top: 420px;
    display: flex; align-items: center; gap: 10px; color: var(--logo-blue); font-weight: 600;
  }
  .brand-dot { width: 46px; height: 46px; border-radius: 50%; border: 2px solid var(--logo-blue); }
  .brand-name { font-size: 24px; line-height: 24px; letter-spacing: 0.5px; }
  .brand-sub { font-size: 9px; line-height: 14px; letter-spacing: 0.3px; }
</style>
</head>
<body>

<section class="card card--front">
  <svg class="front-band" width="657" height="500" viewBox="0 0 657 500" aria-hidden="true">
    <polygon points="0,451 657,81 657,500 0,500" fill="var(--brand-blue)"/>
  </svg>

  <div class="city-art" role="img" aria-label="Isometric illustration of white city buildings, houses and trees rising in height"></div>

  <h1 class="headline">
    <span class="hl-blue">Monthly income</span><br>
    without <strong>tenant</strong><br>
    <strong>headaches</strong>
  </h1>

  <ul class="benefits">
    <li>Formal protection as a lien holder against home</li>
    <li>No commission or closing cost</li>
    <li>Fast closings possible</li>
    <li>Property taken as is so no repairs</li>
  </ul>

  <div class="pct pct--100">100<sup>%</sup></div>
  <div class="pct pct--110">110<sup>%</sup></div>
  <div class="pct pct--160">160<sup>%</sup></div>
  <div class="pct-caption">of market<br>value<br>for your<br>property</div>
</section>

<section class="card card--back">
  <div class="skyline" role="img" aria-label="Faint city skyline silhouette"></div>

  <p class="intro">It’s simple. I am a new investor without down payment capital who still want to double our portfolio this year to grow our portfolio.</p>

  <p class="option option--one">Option 1, you can receive 80% now cash and 30% over a short period of time including interest.</p>
  <p class="option option--two">Option 2, where act like a bank allowing you to make 150% if you finance the whole property(ies). No gimmicks and surprises, just simple unconventional financing.</p>

  <div class="brand">
    <span class="brand-dot"></span>
    <div>
      <div class="brand-name">HELIX</div>
      <div class="brand-sub">REAL ESTATE GROUP</div>
    </div>
  </div>
</section>

</body>
</html>
```